Financial Coaching & Personal Development

I’m desiring a classic business card for my financial coaching and personal development business. The colors I have started with are a goldish brown and hunter green. The brownish color represents soil and green represents growth. I don’t want it it to look masculine. I want the brown to be more of a golden color. I want the color combination and overall design to be timeless not trendy. The logo can be changed as long as it represents growth- moving from where you are to where you want to be.

Target Market(s)

Working Adults with median income $65k; small businesses with a minimum of 20 employees

Industry/Entity Type

Consulting

Contact Information for Business Card

Marla Pettit, MBA
Certified Financial Coach

Font styles to use
Serif

Requirements
Must have
• Logo
My name
Business description
Email marla.pettit@brightwaycoachhub
Phone number 555-314-7829
Nice to have
• Slogan

```html
<!DOCTYPE html>
<html lang="en">
<head>
<meta charset="utf-8">
<title>Brightway Coach Hub – Business Card</title>
<link href="https://fonts.googleapis.com/css2?family=Libre+Baskerville:wght@400;700&display=swap" rel="stylesheet">
<style>
  :root{
    --paper:#e8e8f3;
    --gold:#6b5a26;
    --gold-light:#8a7535;
    --green:#21884a;
    --ink:#3a3a3a;
    --stage:#ecebe6;
    --white:#ffffff;
  }
  *{margin:0;padding:0;box-sizing:border-box}
  html,body{width:1200px;height:892px;overflow:hidden}
  body{background:var(--stage);font-family:"Libre Baskerville",serif;color:var(--ink);position:relative}
  .card{position:absolute;left:290px;width:620px;height:354px;box-shadow:0 6px 18px rgba(0,0,0,.18)}
  .card-front{top:68px;background:var(--paper);overflow:hidden}
  .card-back{top:470px;background:var(--gold);overflow:hidden}

  .brand{position:absolute;left:48px;top:112px;width:240px;text-align:left}
  .brand-row{display:flex;align-items:center;gap:10px}
  .brand-mark{width:20px;height:20px;background:var(--green)}
  .brand-name{font-weight:700;font-size:19px;color:var(--gold);letter-spacing:.5px;text-transform:uppercase;line-height:1.2}
  .brand-tagline{margin-top:8px;font-size:10.5px;color:var(--green)}

  .divider{position:absolute;left:300px;top:60px;width:1px;height:178px;background:#9a9aa5}

  .person{position:absolute;left:330px;top:64px}
  .person-name{font-weight:700;font-size:22px;color:var(--gold)}
  .person-title{font-size:14px;color:var(--ink);margin-top:4px}
  .contact{list-style:none;margin-top:30px;font-size:12.5px}
  .contact li{display:flex;align-items:center;gap:9px;margin-bottom:7px}
  .contact svg{width:12px;height:12px;fill:var(--gold);flex:none}

  .slogan-band{position:absolute;left:0;right:0;bottom:24px;height:42px;background:var(--gold);display:flex;align-items:center;padding-left:40px;color:var(--white);font-size:13.5px}
  .slogan-band strong{font-weight:700;margin:0 4px}
  .band-accent{position:absolute;right:0;bottom:24px;width:82px;height:42px;background:var(--green);display:flex;align-items:center;justify-content:center}
  .band-accent span{width:16px;height:16px;border:2px solid var(--white)}

  .back-pattern{position:absolute;inset:0;background:linear-gradient(135deg,#6f5e29,#5f5022 60%,#736231)}
  .back-brand{position:absolute;left:0;right:0;top:150px;text-align:center;color:var(--white);font-weight:700;font-size:22px;letter-spacing:1px;text-transform:uppercase}
</style>
</head>
<body>
  <section class="card card-front">
    <div class="brand">
      <div class="brand-row">
        <span class="brand-mark"></span>
        <span class="brand-name">Brightway Coach Hub</span>
      </div>
      <p class="brand-tagline">Financial Education &amp; Personal Development</p>
    </div>

    <div class="divider"></div>

    <div class="person">
      <p class="person-name">Marla Pettit, MBA</p>
      <p class="person-title">Certified Financial Coach</p>
      <ul class="contact">
        <li><svg viewBox="0 0 24 24"><path d="M6.6 10.8a15 15 0 0 0 6.6 6.6l2.2-2.2c.3-.3.7-.4 1-.2 1.1.4 2.3.6 3.6.6.6 0 1 .4 1 1V20c0 .6-.4 1-1 1A17 17 0 0 1 3 4c0-.6.4-1 1-1h3.5c.6 0 1 .4 1 1 0 1.3.2 2.5.6 3.6.1.3 0 .7-.2 1z"/></svg>555-314-7829</li>
        <li><svg viewBox="0 0 24 24"><path d="M2 5h20v14H2zm2 2v.5l8 5 8-5V7l-8 5z"/></svg>marla.pettit@brightwaycoachhub.com</li>
        <li><svg viewBox="0 0 24 24"><path d="M12 2a10 10 0 1 0 0 20 10 10 0 0 0 0-20zm6.9 9h-3a15 15 0 0 0-1.3-5.5A8 8 0 0 1 18.9 11zM12 4c.9 1.3 1.8 3.8 1.9 7h-3.8c.1-3.2 1-5.7 1.9-7zM9.4 5.5A15 15 0 0 0 8.1 11h-3a8 8 0 0 1 4.3-5.5zM5.1 13h3a15 15 0 0 0 1.3 5.5A8 8 0 0 1 5.1 13zM12 20c-.9-1.3-1.8-3.8-1.9-7h3.8c-.1 3.2-1 5.7-1.9 7zm2.6-1.5a15 15 0 0 0 1.3-5.5h3a8 8 0 0 1-4.3 5.5z"/></svg>www.brightwaycoachhub.com</li>
      </ul>
    </div>

    <div class="slogan-band">Create a<strong>Financial Plan</strong>that makes you Smile!</div>
    <div class="band-accent"><span></span></div>
  </section>

  <section class="card card-back">
    <div class="back-pattern" role="img" aria-label="Tone-on-tone repeating pattern of the brand mark in golden brown"></div>
    <p class="back-brand">Brightway Coach Hub</p>
  </section>
</body>
</html>
```